Banners for a bowtie/tie Fashion shop

I need banners (770x100) for a necktie and bowtie shop (http://www.kelorin.dk)

5 BOWTIE BANNERS:

I need the 3 text versions for eatch bowtie banner:

Danmarks største udvalg af butterfly
Køb butterfly. FRI fragt og FRI retur
Butterfly fra 199,- inkl. FRI fragt

5 NECKTIE BANNERS:

I need the 3 text versions for eatch necktie banner:

Danmarks største udvalg af slips
Køb slips. FRI fragt og FRI retur
Slips fra 199,- inkl. FRI fragt

All banners should contain the logo. All in JPG format and Photoshop/Inddesign/illustrator format

Target Market(s)

Guys and Gays

Industry/Entity Type

Shop

Requirements
Must have
• Logo
Nice to have
• Nice new pictures

```html
<!DOCTYPE html>
<html lang="da">
<head>
<meta charset="utf-8">
<title>Kelorin – butterfly banner</title>
<link rel="stylesheet" href="https://fonts.googleapis.com/css2?family=Open+Sans:wght@600;700&display=swap">
<style>
  :root {
    --bg-light: #dfe9e8;
    --bg-teal: #c7dcdb;
    --photo-light: #eef0ee;
    --photo-mid: #d4d8d6;
    --photo-dark: #a9b0b0;
    --headline-red: #d31a3d;
    --product-salmon: #f0846b;
    --text-white: #ffffff;
    --brand-grey: #3b3f42;
  }
  html, body {
    margin: 0;
    padding: 0;
    overflow: hidden;
  }
  body {
    width: 1200px;
    height: 156px;
    font-family: "Open Sans", Arial, sans-serif;
  }
  .banner {
    position: relative;
    width: 1200px;
    height: 156px;
    overflow: hidden;
    background: linear-gradient(90deg, var(--bg-light) 0%, var(--bg-teal) 55%, var(--bg-light) 62%);
  }
  .banner__photo {
    position: absolute;
    top: 0;
    right: 0;
    width: 540px;
    height: 156px;
    background: linear-gradient(90deg, rgba(238,240,238,0) 0%, var(--photo-light) 22%, var(--photo-mid) 60%, var(--photo-dark) 100%);
  }
  .headline {
    position: absolute;
    left: 16px;
    top: 19px;
    height: 59px;
    padding: 0 18px 0 14px;
    background: var(--headline-red);
    color: var(--text-white);
    font-weight: 600;
    font-size: 34px;
    line-height: 59px;
    letter-spacing: -0.2px;
    white-space: nowrap;
  }
  .product {
    position: absolute;
    left: 402px;
    top: 86px;
    width: 209px;
    height: 57px;
    background: var(--product-salmon);
    color: var(--text-white);
    font-weight: 600;
    font-size: 41px;
    line-height: 55px;
    text-align: center;
  }
  .brand {
    position: absolute;
    left: 28px;
    top: 98px;
    color: var(--brand-grey);
    font-weight: 700;
    font-size: 32px;
    line-height: 40px;
    letter-spacing: -0.5px;
  }
</style>
</head>
<body>
  <div class="banner">
    <div class="banner__photo" role="img" aria-label="Photo of a man in a white shirt with a checked bowtie and black suspenders"></div>
    <div class="headline">Danmarks største udvalg af</div>
    <div class="product">butterfly</div>
    <div class="brand">kelorin</div>
  </div>
</body>
</html>
```